Cover-Design für Buch über Corona-Pandemie
Zielgruppe
Ich bin ein junger Arzt und schreibe ein Buch über die Corona Pandemie. Zielgruppe sind alle Menschen, die sich kritisch aber seriös mit der Thematik befassen. Ich werde das Buch selbst veröffentlichen über Buchwelt oder ähnliche Portale.
Aufgabenstellung
Sehr geehrte Designer,
ich hätte gern das Buchcover mit Vorderseite und Hinterseite. Die beiden Textvorlagen befinden sich in der hochgeladenen Datei. Seite 1 ist die Vorderseite, Seite 2 die Hinterseite des Buchcovers.
Sie können sich grob an dem Buchcover 'Fieber Irrtum' von Wendorf orientieren. Also ein sehr großer Titel in rot, schlicht gestaltet, unter dem Titel der Untertitel in schwarz, so wie in der angehängten Datei. Der Titel sollte ebenfalls auf zwei Zeilen in großer Schrift aufgeteilt sein wie von Wendorf. Der Autorenname sollte ganz unten auf der Coverseite zentral seinTitel, Untertitel und Autorenname sollten ca. 60% der Länge des Buchcovers ausmachen. Die Ähnlichkeit zum Wendorf Buch sollte wegen dem Urheberrecht nicht zu groß ist, aber da kennen Sie sich sicher besser aus und können sicher entsprechende Modifikationen machen. So kann man ja z.B Weinrot verwenden oder andere Formatierungen.
Darunter hätte ich gerne ein Gehirn, mit Injektionsspritzen, die in das Gehirn stechen und wie ein Kranz um das Gehirn gereiht sind Daneben sollte ein CoronaVirus sein, dessen Hülle dem Gehirn mit den Spritzen sehr ähnlich sieht. Beides in Schwarz-Weiß. Als grobe Orientierungshilfe habe ich selbst ein Gehirn mit den Spritzen in der Datei entworfen, damit Sie eine ungefähre Idee von der Optik haben.
Wenn Sie echte Abbildungen von Gehirn und Spritzen finden und sie in der Bildbearbeitung so nach meiner Vorlage gestalten können, wäre es am Schönsten. Sonst können sie einfach auch Symbole oder Comics wie ich verwenden, solange das Gehirn und das Virus optisch zusammenpassen und den gleichen Stil haben.
Sonst i Stil klare Linien, Minimalistisch.
Auf der Hinterseite des Cover sollte wie in der angehängten Datei das Zitat rot sein, der Text schwarz, sonst habe ich keine weiteren Wünsche.
Vielen Dank!
UPDATE: Zusätzliche hätte ich gerne ein Bild von mir und den Text über den Autor auf der Hinter..

```html
<!DOCTYPE html>
<html lang="de">
<head>
<meta charset="utf-8">
<title>Fieber Taumel? – Buchcover</title>
<link href="https://fonts.googleapis.com/css2?family=Roboto+Condensed:ital,wght@0,400;0,700;1,400;1,700&family=Roboto:ital,wght@0,400;1,700&display=swap" rel="stylesheet">
<style>
  :root {
    --stage: #ececec;
    --paper: #ffffff;
    --title-red: #e0221f;
    --ink: #2b2b2b;
    --illustration-grey: #5f5f63;
    --photo-blue: #8fa3b8;
  }
  * { box-sizing: border-box; margin: 0; padding: 0; }
  html, body { width: 1200px; height: 1128px; overflow: hidden; }
  body {
    background: var(--stage);
    font-family: "Roboto Condensed", "Arial Narrow", sans-serif;
    color: var(--ink);
    position: relative;
  }
  .cover {
    position: absolute;
    top: 164px;
    width: 540px;
    height: 800px;
    background: var(--paper);
    box-shadow: 0 10px 30px rgba(0,0,0,.12);
    overflow: hidden;
  }
  .cover--front { left: 40px; }
  .cover--back { left: 620px; }

  /* Front */
  .title {
    position: absolute;
    top: 56px; left: 0; right: 0;
    text-align: center;
    color: var(--title-red);
    font-weight: 700;
    line-height: .92;
    letter-spacing: -1px;
  }
  .title__line1 { display: block; font-size: 132px; }
  .title__line2 { display: block; font-size: 100px; }
  .subtitle {
    position: absolute;
    top: 292px; left: 0; right: 0;
    text-align: center;
    font-size: 17px;
    line-height: 1.2;
    color: var(--ink);
  }
  .artwork {
    position: absolute;
    top: 370px; left: 36px;
    width: 468px; height: 300px;
  }
  .author-front {
    position: absolute;
    bottom: 38px; left: 0; right: 0;
    text-align: center;
    font-family: "Roboto", sans-serif;
    font-style: italic;
    font-weight: 700;
    font-size: 21px;
  }

  /* Back */
  .back-decor {
    position: absolute;
    top: 10px; left: 130px;
    width: 380px; height: 380px;
  }
  .author-photo {
    position: absolute;
    top: 76px; left: 24px;
    width: 142px; height: 182px;
  }
  .quote {
    position: absolute;
    top: 90px; left: 188px; right: 28px;
    color: var(--title-red);
    font-style: italic;
    font-size: 17px;
    line-height: 1.38;
    text-align: justify;
  }
  .blurb {
    position: absolute;
    top: 284px; left: 22px; right: 28px;
    font-size: 16.5px;
    line-height: 1.45;
    text-align: justify;
    hyphens: auto;
  }
  .blurb p + p { margin-top: 8px; }
  .author-back {
    position: absolute;
    top: 690px; right: 28px;
    font-family: "Roboto", sans-serif;
    font-style: italic;
    font-weight: 700;
    font-size: 15px;
  }
  .author-bio {
    position: absolute;
    top: 718px; left: 170px; right: 28px;
    font-size: 11px;
    line-height: 1.4;
    text-align: right;
  }
</style>
</head>
<body>
  <section class="cover cover--front">
    <h1 class="title">
      <span class="title__line1">FIEBER</span>
      <span class="title__line2">TAUMEL?</span>
    </h1>
    <p class="subtitle">Wie Meinungsmanagement und logische<br>Fehlschlüsse unser Denken vergiften</p>
    <svg class="artwork" role="img" aria-label="Illustration: Gehirn mit einem Kranz aus Injektionsspritzen und daneben ein Virus, beides in Grau" viewBox="0 0 468 300">
      <defs>
        <radialGradient id="artTone" cx="40%" cy="50%" r="60%">
          <stop offset="0" stop-color="#6a6a6e"/>
          <stop offset="1" stop-color="#d9d9db"/>
        </radialGradient>
      </defs>
      <rect width="468" height="300" fill="url(#artTone)" opacity=".35"/>
    </svg>
    <p class="author-front">Dr. med. univ. Jonas Wieland</p>
  </section>

  <section class="cover cover--back">
    <svg class="back-decor" role="img" aria-label="Blasse Virusgrafik im Hintergrund" viewBox="0 0 380 380">
      <defs>
        <radialGradient id="decorTone" cx="50%" cy="50%" r="50%">
          <stop offset="0" stop-color="#e6e6e6"/>
          <stop offset="1" stop-color="#ffffff"/>
        </radialGradient>
      </defs>
      <rect width="380" height="380" fill="url(#decorTone)"/>
    </svg>
    <svg class="author-photo" role="img" aria-label="Porträtfoto des Autors vor blaugrauem Hintergrund" viewBox="0 0 142 182">
      <defs>
        <linearGradient id="photoTone" x1="0" y1="0" x2="0" y2="1">
          <stop offset="0" stop-color="#9aabbd"/>
          <stop offset="1" stop-color="#5f8fc4"/>
        </linearGradient>
      </defs>
      <rect width="142" height="182" fill="url(#photoTone)"/>
    </svg>
    <p class="quote">„Die bewusste und zielgerichtete Manipulation der Verhaltensweisen und Einstellungen der Massen ist ein wesentlicher Bestandteil westlicher Demokratien.“</p>
    <div class="blurb">
      <p>Schon der Begründer der Public Relations und Neffe von Siegfried Brandt, Edmund Barlow, erkannte 1928 die zentrale Rolle des Meinungsmanagements, das aktueller denn je ist.</p>
      <p>Die Pandemie reißt gewaltige Gräben innerhalb unserer Gesellschaft auf. Emotionalisierung, Moralisierung und Manipulation vergiften die inhaltliche Diskussion von Mensch zu Mensch, die Basis von Wissenschaft, Demokratie und Beziehungen. Dieser verzerrte Diskurs verlegt Lösungswege aus der Pandemie.</p>
      <p>Das Buch zeigt viele etablierte Manipulationstechniken, die seit Jahrzehnten von Politik, Medien und Wirtschaft angewendet werden, um die öffentliche Meinung zu beeinflussen. Außerdem beleuchtet es logische Fehlschlüsse, die viele Argumentationen ungültig machen.</p>
    </div>
    <p class="author-back">Dr. med. univ. Jonas Wieland</p>
    <p class="author-bio">Geboren 1992 in der Obersteiermark, arbeitet als Arzt in Ausbildung zum Allgemeinmediziner in einer Wiener Klinik. Er erlebt als junger Mediziner die Pandemie an vorderster Front.</p>
  </section>
</body>
</html>
```